Business Card Design

Recruitment Company. Want to keep the logo and the green colour

Industry/Entity Type

Business

Contact Information for Business Card

Hi,

1.)
MARTIN HOLLOWAY
Director
Level 6, 248 Finch Street
Brisbane QLD 4000
M 0412 630 574
E martin@tallonstaffing.com.au
www.tallonstaffing.com.au

2.)
TOM WAVERLEY
Director
Level 6, 248 Finch Street
Brisbane QLD 4000
M 0419 247 613
E tom@tallonstaffing.com.au

Want something different and eye catching, happy for you guys to use your design flare to work some magic with these.

Many Thanks
Tom

```html
<!DOCTYPE html>
<html lang="en">
<head>
<meta charset="utf-8">
<title>Tallon Staffing — Business Cards</title>
<link rel="stylesheet" href="https://fonts.googleapis.com/css2?family=Open+Sans:wght@400;700&display=swap">
<style>
  :root {
    --lime: #b2cd45;
    --charcoal: #2c2c2e;
    --charcoal-light: #3b3b3d;
    --ink: #1e1e1e;
    --link: #2438c8;
    --page: #ffffff;
    --card-w: 333px;
    --card-h: 210px;
  }
  * { box-sizing: border-box; margin: 0; padding: 0; }
  html, body { width: 691px; height: 1200px; overflow: hidden; background: var(--page); }
  body { font-family: "Open Sans", Arial, sans-serif; color: var(--ink); position: relative; }

  .card {
    position: absolute;
    width: var(--card-w);
    height: var(--card-h);
    background: var(--lime);
    overflow: hidden;
  }
  .card__art { position: absolute; inset: 0; width: 100%; height: 100%; }

  .card--front-martin-a { left: 0;     top: 0; }
  .card--back-martin-a  { left: 0;     top: 244px; }
  .card--front-martin-b { left: 357px; top: 244px; }
  .card--front-tom-a    { left: 0;     top: 494px; }
  .card--back-martin-b  { left: 357px; top: 488px; }
  .card--back-tom-a     { left: 0;     top: 743px; }
  .card--front-tom-b    { left: 357px; top: 743px; }
  .card--back-tom-b     { left: 357px; top: 990px; }

  .brand {
    position: absolute; left: 36px; top: 9px;
    font-weight: 700; font-size: 21px; letter-spacing: -0.3px;
    color: var(--ink); text-transform: uppercase;
  }
  .holder { position: absolute; left: 27px; top: 82px; }
  .holder__name { font-size: 22px; font-weight: 400; line-height: 1.1; }
  .holder__role { font-size: 10px; line-height: 1.2; }
  .contact { position: absolute; left: 27px; top: 131px; font-size: 7.3px; line-height: 9.4px; }
  .contact__email { color: var(--link); text-decoration: underline; }

  .back-name {
    position: absolute; left: 247px; top: 123px;
    transform: translate(-50%, -50%) rotate(-68deg);
    font-size: 21px; white-space: nowrap; color: var(--ink);
  }
</style>
</head>
<body>

<!-- Front, Martin -->
<section class="card card--front-martin-a">
  <svg class="card__art" viewBox="0 0 250 157" preserveAspectRatio="none" role="img" aria-label="Dark textured diagonal band">
    <defs><linearGradient id="texA" x1="0" y1="0" x2="1" y2="1"><stop offset="0" stop-color="#3b3b3d"/><stop offset="1" stop-color="#242426"/></linearGradient></defs>
    <polygon points="177,0 181,0 144,157 140,157" fill="url(#texA)"/>
    <polygon points="187,0 250,0 250,157 150,157" fill="url(#texA)"/>
  </svg>
  <div class="brand">Tallonstaffing</div>
  <div class="holder"><div class="holder__name">Martin Holloway</div><div class="holder__role">director level 6</div></div>
  <div class="contact">Your addres<br>Phone : 0412 630 574<br>email : <span class="contact__email">martin@tallonstaffing.com.au</span><br>248 Finch Street Brisbane QLD 4000 M<br>www.tallonstaffing.co.au</div>
</section>

<!-- Back, Martin -->
<section class="card card--back-martin-a">
  <svg class="card__art" viewBox="0 0 250 157" preserveAspectRatio="none" role="img" aria-label="Dark textured diagonal panel">
    <defs><linearGradient id="texB" x1="0" y1="0" x2="1" y2="1"><stop offset="0" stop-color="#3b3b3d"/><stop offset="1" stop-color="#242426"/></linearGradient></defs>
    <polygon points="0,0 181,0 146,157 0,157" fill="url(#texB)"/>
    <polygon points="185,0 190,0 155,157 150,157" fill="url(#texB)"/>
  </svg>
  <div class="back-name">Martin Holloway</div>
</section>

<!-- Front, Martin -->
<section class="card card--front-martin-b">
  <svg class="card__art" viewBox="0 0 250 157" preserveAspectRatio="none" role="img" aria-label="Dark textured diagonal band">
    <polygon points="177,0 181,0 144,157 140,157" fill="url(#texA)"/>
    <polygon points="187,0 250,0 250,157 150,157" fill="url(#texA)"/>
  </svg>
  <div class="brand">Tallonstaffing</div>
  <div class="holder"><div class="holder__name">Martin Holloway</div><div class="holder__role">director level 6</div></div>
  <div class="contact">Your addres<br>Phone : 0412 630 574<br>email : <span class="contact__email">martin@tallonstaffing.com.au</span><br>248 Finch Street Brisbane QLD 4000 M<br>www.tallonstaffing.co.au</div>
</section>

<!-- Front, Tom -->
<section class="card card--front-tom-a">
  <svg class="card__art" viewBox="0 0 250 157" preserveAspectRatio="none" role="img" aria-label="Dark textured diagonal band">
    <polygon points="177,0 181,0 144,157 140,157" fill="url(#texA)"/>
    <polygon points="187,0 250,0 250,157 150,157" fill="url(#texA)"/>
  </svg>
  <div class="brand">Tallonstaffing</div>
  <div class="holder"><div class="holder__name">Tom Waverley</div><div class="holder__role">director level 6</div></div>
  <div class="contact">Your addres<br>Phone : 0419 247 613<br>email : <span class="contact__email">tom@tallonstaffing.com.au</span><br>248 Finch Street Brisbane QLD 4000 M<br>www.tallonstaffing.co.au</div>
</section>

<!-- Back, Martin -->
<section class="card card--back-martin-b">
  <svg class="card__art" viewBox="0 0 250 157" preserveAspectRatio="none" role="img" aria-label="Dark textured diagonal panel">
    <polygon points="0,0 181,0 146,157 0,157" fill="url(#texB)"/>
    <polygon points="185,0 190,0 155,157 150,157" fill="url(#texB)"/>
  </svg>
  <div class="back-name">Martin Holloway</div>
</section>

<!-- Back, Tom -->
<section class="card card--back-tom-a">
  <svg class="card__art" viewBox="0 0 250 157" preserveAspectRatio="none" role="img" aria-label="Dark textured diagonal panel">
    <polygon points="0,0 181,0 146,157 0,157" fill="url(#texB)"/>
    <polygon points="185,0 190,0 155,157 150,157" fill="url(#texB)"/>
  </svg>
  <div class="back-name">Tom Waverley</div>
</section>

<!-- Front, Tom -->
<section class="card card--front-tom-b">
  <svg class="card__art" viewBox="0 0 250 157" preserveAspectRatio="none" role="img" aria-label="Dark textured diagonal band">
    <polygon points="177,0 181,0 144,157 140,157" fill="url(#texA)"/>
    <polygon points="187,0 250,0 250,157 150,157" fill="url(#texA)"/>
  </svg>
  <div class="brand">Tallonstaffing</div>
  <div class="holder"><div class="holder__name">Tom Waverley</div><div class="holder__role">director level 6</div></div>
  <div class="contact">Your addres<br>Phone : 0419 247 613<br>email : <span class="contact__email">tom@tallonstaffing.com.au</span><br>248 Finch Street Brisbane QLD 4000 M<br>www.tallonstaffing.co.au</div>
</section>

<!-- Back, Tom -->
<section class="card card--back-tom-b">
  <svg class="card__art" viewBox="0 0 250 157" preserveAspectRatio="none" role="img" aria-label="Dark textured diagonal panel">
    <polygon points="0,0 181,0 146,157 0,157" fill="url(#texB)"/>
    <polygon points="185,0 190,0 155,157 150,157" fill="url(#texB)"/>
  </svg>
  <div class="back-name">Tom Waverley</div>
</section>

</body>
</html>
```